smile partners of lakeview | ||
business cards/stationary | ||
Cutting-Edge Professional |
Dr. Marcus Holloway / Dr. Leonardo Brisco | ||
President | ||
Bayonne 57 Ave K Bayonne, NJ 07002 201-555-0142 ********* East Orange 42 North Whitfield St Suite 208 East Orange, NJ 07018 973-555-0187 ******** North Bergen 4829 Larkmoor North Bergen, NJ 07047 201-555-0163 ********** Union City 2748 Quenton Ave Union City, NJ 07087 201-555-0129 ********* Paterson 3170 Elm street Suite K Paterson, NJ 07503 973 555-0114 ******** |
office@quentondental.example | ||
www.SmilePartnersOfLV.example | ||
We need 7 different business card designs. 1. Dr Marcus Holloway (no address..just website) 2. Dr Leonardo Brisco (no address just website) 3. Smile Partners of Lakeview - East Orange 4. Smile Partners of Lakeview - Bayone 5. Smile Partners of Lakeview- Union City 6. Smile Partners of Lakeview- North Bergen 7. Smile Partners of Lakeview- Paterson Business Cards 3-7 do not need to include Dr Holloway/Dr Brisco's name on them |
For the personal cards (Dr Marcus Holloway and Dr Leo Brisco) use the back of the cards to tell all of the office locations For the Office cards (3-7) use the back of the card for appointments...we will upload a sample background that we currently use. |
554611_1195_4351.png |
photo3_JPG4352.jpg |
DentalGroups_Paterson_4421.pdf |
DentalGroups_Paterson_4422.gif |
DentalGroups_Paterson_4423.eps |
DentalGroups_Web_4424.png |
DentalGroups_Web_4425.ai |
DentalGroups_Web_4426.gif |

```html
<!DOCTYPE html>
<html lang="en">
<head>
<meta charset="utf-8">
<title>Smile Partners of Lakeview – Business Card</title>
<link rel="stylesheet" href="https://fonts.googleapis.com/css2?family=Tinos:wght@400;700&display=swap">
<style>
  :root {
    --brown: #6a4a22;
    --brown-dark: #3e2a10;
    --gold: #c9a25a;
    --gold-light: #e9d3a4;
    --ink: #333;
    --rule: #9a9a9a;
    --edge: #cfcfcf;
    --paper: #fff;
  }
  * { box-sizing: border-box; margin: 0; padding: 0; }
  html, body { width: 1200px; height: 334px; overflow: hidden; background: var(--paper); }
  body { position: relative; font-family: "Tinos", "Times New Roman", serif; color: var(--ink); }

  .card { position: absolute; top: 0; height: 334px; width: 588px; border: 1px solid var(--edge); background: var(--paper); overflow: hidden; }
  .card--front { left: 0; }
  .card--back { left: 612px; }

  /* Front */
  .brand { position: absolute; left: 22px; top: 150px; width: 270px; }
  .brand__name { font-size: 34px; line-height: 36px; font-weight: 700; color: var(--brown); }
  .brand__web { margin-top: 8px; font-size: 9px; color: var(--brown); }

  .divider { position: absolute; left: 306px; top: 78px; width: 1px; height: 180px; background: var(--gold); }

  .contact { position: absolute; left: 322px; top: 82px; font-size: 12px; line-height: 15px; color: var(--ink); }
  .contact__name { color: var(--brown); }
  .contact__block { margin-top: 14px; }

  .band { position: absolute; left: 0; right: 0; bottom: 0; height: 40px;
    background: linear-gradient(180deg, var(--gold-light) 0%, var(--gold) 30%, var(--brown) 65%, var(--brown-dark) 100%); }

  /* Back */
  .appt__title { position: absolute; top: 14px; left: 0; right: 0; text-align: center; font-size: 28px; }
  .field { position: absolute; left: 34px; right: 34px; border-bottom: 1px solid var(--rule); font-size: 15px; padding-bottom: 4px; }
  .field--for { top: 76px; }
  .field--date { top: 218px; }
  .field__time { position: absolute; left: 310px; }

  .days { position: absolute; top: 140px; left: 34px; right: 34px; display: flex; justify-content: space-between; }
  .day { display: flex; align-items: center; gap: 5px; font-size: 14px; }
  .day__box { width: 17px; height: 17px; border: 1px solid var(--ink); }

  .appt__note { position: absolute; bottom: 20px; left: 0; right: 0; text-align: center; font-size: 14px; }
</style>
</head>
<body>
  <section class="card card--front">
    <div class="brand">
      <div class="brand__name">Smile Partners<br>of Lakeview</div>
      <div class="brand__web">www.SmilePartnersOfLV.example</div>
    </div>
    <div class="divider"></div>
    <div class="contact">
      <div class="contact__name">Dr. Marcus Holloway</div>
      <div>President</div>
      <div class="contact__block">3170 Elm street<br>Suite K<br>Paterson, NJ 07503<br>973 555-0114</div>
      <div class="contact__block">Email : office@quentondental.example<br>Web : www.SmilePartnersOfLV.example</div>
    </div>
    <div class="band"></div>
  </section>

  <section class="card card--back">
    <h1 class="appt__title" style="font-weight:400">Appointment</h1>
    <div class="field field--for">For</div>
    <div class="days">
      <div class="day"><span class="day__box"></span>Mon</div>
      <div class="day"><span class="day__box"></span>Tue</div>
      <div class="day"><span class="day__box"></span>Wed</div>
      <div class="day"><span class="day__box"></span>Thr</div>
      <div class="day"><span class="day__box"></span>Fri</div>
      <div class="day"><span class="day__box"></span>Sat</div>
      <div class="day"><span class="day__box"></span>Sun</div>
    </div>
    <div class="field field--date">Date<span class="field__time">Time</span></div>
    <p class="appt__note">If You are Unable to keep this Appointment, Please Notice use for 24 hours</p>
  </section>
</body>
</html>
```